Sticker Design

I need a unique logo for a CIRCULAR sticker for musical artist, Crondel Vaux. I have attached two styles the artist prefers. The design should be circular. It should feature prominently "Crondel Vaux" and have his website smaller at the bottom "www.crondelvaux.net." The design should have a black or dark background. The artist is interested in seeing his name in a neon style (pink). But he would consider something else original, in line with, but not exactly the same as, the other reference supplied. This is a guaranteed project. Thank you for your talents.

```html
<!DOCTYPE html>
<html lang="en">
<head>
<meta charset="utf-8">
<title>Crondel Vaux — Sticker</title>
<link rel="stylesheet" href="https://fonts.googleapis.com/css2?family=Oswald:wght@300;400&display=swap">
<style>
  :root {
    --page: #ffffff;
    --sticker: #050505;
    --portrait-light: #3a3a3a;
    --portrait-dark: #0a0a0a;
    --neon: #e8127c;
    --neon-glow: rgba(255, 40, 150, 0.85);
    --echo: #9c6f86;
    --url: #f2f2f2;
  }
  html, body {
    margin: 0;
    width: 1200px;
    height: 1200px;
    overflow: hidden;
    background: var(--page);
  }
  .sticker {
    display: block;
    width: 1200px;
    height: 1200px;
  }
  .sticker__disc { fill: var(--sticker); }
  .sticker__url {
    font-family: "Oswald", sans-serif;
    font-weight: 400;
    font-size: 40px;
    fill: var(--url);
    letter-spacing: 1px;
  }
  .sticker__name {
    font-family: "Oswald", sans-serif;
    font-weight: 300;
    font-size: 128px;
    fill: var(--neon);
    filter: drop-shadow(0 0 6px var(--neon-glow)) drop-shadow(0 0 18px var(--neon-glow));
  }
  .sticker__name-echo {
    font-family: "Oswald", sans-serif;
    font-weight: 300;
    font-size: 56px;
    fill: var(--echo);
  }
</style>
</head>
<body>
<svg class="sticker" viewBox="0 0 1200 1200" xmlns="http://www.w3.org/2000/svg">
  <defs>
    <clipPath id="disc-clip">
      <circle cx="601" cy="601" r="455"/>
    </clipPath>
    <radialGradient id="portrait-tone" cx="0.62" cy="0.55" r="0.6">
      <stop offset="0" stop-color="#3a3a3a"/>
      <stop offset="1" stop-color="#0a0a0a"/>
    </radialGradient>
    <linearGradient id="portrait-fade" x1="0" x2="1" y1="0" y2="0">
      <stop offset="0" stop-color="#050505" stop-opacity="1"/>
      <stop offset="0.35" stop-color="#050505" stop-opacity="0"/>
    </linearGradient>
  </defs>

  <circle class="sticker__disc" cx="601" cy="601" r="455"/>

  <g class="sticker__portrait" clip-path="url(#disc-clip)" role="img" aria-label="Dark portrait photo of the artist wearing sunglasses">
    <rect x="560" y="146" width="500" height="910" fill="url(#portrait-tone)"/>
    <rect x="560" y="146" width="500" height="910" fill="url(#portrait-fade)"/>
  </g>

  <text class="sticker__name" x="229" y="540" textLength="571" lengthAdjust="spacingAndGlyphs">CRONDEL VAUX</text>
  <text class="sticker__name-echo" x="268" y="618" textLength="340" lengthAdjust="spacingAndGlyphs">CRONDEL VAUX</text>

  <text class="sticker__url" x="601" y="900" text-anchor="middle">WWW.CRONDELVAUX.NET.</text>
</svg>
</body>
</html>
```